Baby Shower Invitation for Vectored Image Provided

Caroline & Desmond's Baby Shower - Black/White/Gold Colors preferred
Please use the vectored portrait image attached. I'd like us on the lower right side of the invitation.
Can be horizontal or vertical layout.
The second image attached has the information needed for you to complete.
I don't want that style copied, it is just an example.

```html
<!DOCTYPE html>
<html lang="en">
<head>
<meta charset="utf-8">
<title>Caroline's Baby Shower Invitation</title>
<link href="https://fonts.googleapis.com/css2?family=Great+Vibes&family=Montserrat:wght@300;400;600;800&display=swap" rel="stylesheet">
<style>
  :root {
    --ink: #0b0b0b;
    --paper: #ffffff;
    --gold: #f6c235;
    --text: #1c1c1c;
    --text-light: #3a3a3a;
    --backdrop: #eeeae4;
  }
  html, body { margin: 0; padding: 0; overflow: hidden; background: var(--backdrop); }
  .canvas { width: 1200px; height: 1200px; display: block; }
  .script { font-family: "Great Vibes", cursive; }
  .sans { font-family: "Montserrat", sans-serif; }
  .headline { fill: var(--ink); font-size: 62px; }
  .tagline { fill: var(--gold); font-size: 29px; font-weight: 800; }
  .intro { fill: var(--text); font-size: 23px; font-weight: 600; }
  .honoree { fill: var(--gold); font-size: 54px; }
  .date-month { fill: var(--gold); font-size: 27px; font-weight: 800; }
  .date-day { fill: var(--gold); font-size: 60px; font-weight: 600; }
  .date-weekday { fill: var(--gold); font-size: 23px; font-weight: 600; }
  .detail { fill: var(--text-light); font-size: 25px; font-weight: 300; }
  .rsvp { fill: var(--text); font-size: 20.5px; font-weight: 600; }
  .divider { stroke: var(--text); stroke-width: 3; stroke-dasharray: 9 7; fill: none; }
  .foot-outline { fill: var(--ink); }
  .foot-edge { fill: none; stroke: var(--ink); stroke-width: 70; stroke-linejoin: round; }
  .paper { fill: var(--paper); }
  .registry { fill: var(--paper); font-size: 56px; }
</style>
</head>
<body>
<svg class="canvas" viewBox="0 0 1500 1500" xmlns="http://www.w3.org/2000/svg">
  <defs>
    <linearGradient id="backShade" gradientUnits="userSpaceOnUse" x1="760" y1="320" x2="1380" y2="1260">
      <stop offset="0" stop-color="#0a0a0a"/>
      <stop offset="0.65" stop-color="#111"/>
      <stop offset="1" stop-color="#2c2d2e"/>
    </linearGradient>
    <linearGradient id="portraitTone" x1="0" y1="0" x2="0" y2="1">
      <stop offset="0" stop-color="#8a7566"/>
      <stop offset="1" stop-color="#2d2d30"/>
    </linearGradient>
    <path id="registryCurve" d="M888,1075 C975,1190 1130,1215 1222,1075 C1292,965 1322,835 1338,700"/>
  </defs>

  <!-- Front card -->
  <g class="card-front">
    <path class="foot-outline" d="M103,590 L162,498 L273,425 L411,394 L582,425 L600,560 L150,640 Z"/>
    <path class="foot-edge" d="M370,495 C520,495 625,590 620,720 C615,820 540,860 540,910 C540,960 610,1000 600,1080 C590,1170 500,1210 390,1210 C230,1210 150,1050 130,900 C115,780 140,495 370,495 Z"/>
    <g class="foot-outline">
      <circle cx="103" cy="590" r="58"/>
      <circle cx="162" cy="498" r="64"/>
      <circle cx="273" cy="425" r="72"/>
      <circle cx="411" cy="394" r="72"/>
      <circle cx="582" cy="425" r="108"/>
    </g>
    <path class="paper" d="M370,495 C520,495 625,590 620,720 C615,820 540,860 540,910 C540,960 610,1000 600,1080 C590,1170 500,1210 390,1210 C230,1210 150,1050 130,900 C115,780 140,495 370,495 Z"/>
    <g class="paper">
      <circle cx="103" cy="590" r="42"/>
      <circle cx="162" cy="498" r="48"/>
      <circle cx="273" cy="425" r="55"/>
      <circle cx="411" cy="394" r="55"/>
      <circle cx="582" cy="425" r="90"/>
    </g>

    <text class="script headline" x="380" y="568" text-anchor="middle">Oh Boy !!!</text>
    <text class="sans tagline" x="375" y="612" text-anchor="middle">A LITTLE MAN</text>
    <text class="sans tagline" x="372" y="646" text-anchor="middle">IS ON THE WAY!</text>
    <text class="sans intro" x="370" y="682" text-anchor="middle">Please join us for a</text>
    <text class="sans intro" x="370" y="710" text-anchor="middle">Baby Shower honoring</text>
    <text class="script honoree" x="360" y="760" text-anchor="middle">Caroline Whitmore</text>

    <line class="divider" x1="172" y1="788" x2="555" y2="788"/>
    <line class="divider" x1="316" y1="792" x2="316" y2="930"/>
    <line class="divider" x1="320" y1="834" x2="555" y2="834"/>
    <line class="divider" x1="172" y1="930" x2="520" y2="930"/>

    <text class="sans date-month" x="248" y="820" text-anchor="middle">SEPT</text>
    <text class="sans date-day" x="244" y="880" text-anchor="middle">1</text>
    <text class="sans date-weekday" x="245" y="913" text-anchor="middle">Saturday</text>

    <text class="sans detail" x="333" y="820">11:30am - 2:30pm</text>
    <text class="sans detail" x="333" y="864">The Ashbrook</text>
    <text class="sans detail" x="333" y="890">1847 Carver St.</text>
    <text class="sans detail" x="333" y="917">Raleigh, NC</text>

    <text class="sans rsvp" x="188" y="958">RSVP to Desmond at 0555-123-456</text>
    <text class="sans rsvp" x="188" y="986">by August 20th</text>

    <rect role="img" aria-label="Illustrated portrait of the expecting couple, Caroline and Desmond" x="360" y="968" width="166" height="215" rx="40" fill="url(#portraitTone)"/>
  </g>

  <!-- Back card -->
  <g class="card-back" fill="url(#backShade)">
    <circle cx="830" cy="420" r="90"/>
    <circle cx="1020" cy="395" r="72"/>
    <circle cx="1180" cy="422" r="64"/>
    <circle cx="1300" cy="495" r="55"/>
    <circle cx="1360" cy="590" r="45"/>
    <path d="M745,450 C745,425 790,415 830,420 Q925,440 1020,395 Q1100,430 1180,422 Q1250,460 1300,495 Q1335,545 1360,590 C1385,660 1382,760 1365,860 C1335,1050 1240,1260 1090,1260 C960,1260 845,1190 832,1080 C822,985 878,945 870,885 C862,820 790,780 783,690 C776,600 745,520 745,450 Z"/>
  </g>
  <text class="script registry" textLength="700" lengthAdjust="spacing"><textPath href="#registryCurve">Caroline is registered at Little Nest Baby</textPath></text>
</svg>
</body>
</html>
```